VALTIRO.NET Single Product Based Website

We are one of the largest Stockiest of Diesel Engine (Marine and Power Plants) Spare Parts, this site will be focusing on a Single Product / Spare Parts - Connecting Rods <br/>We attached some actual pictures of the product and the Logo,<br/><br/>Once we approved your design shall provide with some contends and 10 actual Pictures to be added , should be a single page website SEO friendly sources to be used<br/>Should be Desktop, laptop and mobile friendly <br/><br/>best regards<br/>Oliver <br/>

Coding

Coded - Design and coding required

Number of Pages Required

1 page

Font styles to use
Other font styles liked:
• Book Antigua, Book Man Old Style or the designer can suggest

Colors

Designer to choose colors to be used in the design.

Requirements
Must have
• The Logo and same theme / colors can be used
Nice to have
• We shall provide the actual pictures of the product from our gallery approx 10 pictures to be added at final stage
Should not have
• other than initial design purpose , do not use any pictures downloaded from the internet

```html
<!DOCTYPE html>
<html lang="en">
<head>
<meta charset="utf-8">
<title>VALTIRO.NET — Diesel Engine Spare Parts</title>
<link href="https://fonts.googleapis.com/css2?family=Libre+Baskerville:wght@400;700&display=swap" rel="stylesheet">
<style>
:root{
  --blue:#3b5e9d;
  --blue-dark:#2f4f88;
  --orange:#f5693c;
  --light:#eef0f3;
  --dark:#4a4b55;
  --white:#ffffff;
  --ink:#222222;
  --grey:#8e9096;
}
*{box-sizing:border-box;margin:0;padding:0}
html,body{width:1200px;height:4098px;overflow:hidden}
body{font-family:'Libre Baskerville',Georgia,serif;color:var(--ink);background:var(--white);position:relative}
section,header,nav,footer{position:relative;width:1200px;overflow:hidden}
.abs{position:absolute}
.brand{font-weight:700;color:var(--blue);letter-spacing:1px}
.section-title{position:absolute;left:0;width:1200px;text-align:center;font-size:30px;font-weight:700;letter-spacing:1px;color:var(--ink)}
.title-mark{position:absolute;left:597px;width:6px;height:18px;border:2px solid var(--orange);border-radius:3px}

/* header */
.topbar{height:60px;background:var(--white)}
.topbar .brand{position:absolute;left:252px;top:18px;font-size:24px}
.badge{position:absolute;left:551px;top:6px;width:127px;height:45px;background:var(--blue);color:var(--white);text-align:center;font-size:7px;line-height:10px;padding-top:5px}
.badge b{display:block;color:var(--orange);font-size:9px;letter-spacing:1px}
.cart-box{position:absolute;left:687px;top:6px;width:59px;height:45px;background:var(--blue);color:var(--white);text-align:center;font-size:8px;padding-top:8px}
.contact-top{position:absolute;left:789px;font-size:11px;color:var(--blue);white-space:nowrap}
.contact-top i{display:inline-block;width:16px;height:13px;border:1.5px solid var(--orange);border-radius:2px;vertical-align:middle;margin-right:10px}
.mainnav{height:35px;background:var(--orange)}
.mainnav ul{list-style:none;position:absolute;left:245px;top:0;display:flex;height:35px}
.mainnav li{font-size:8.5px;color:var(--white);line-height:35px;padding:0 12px;letter-spacing:.3px}
.mainnav li.active{background:var(--blue);padding:0 18px}

/* hero */
.hero{height:344px;background:linear-gradient(120deg,#9a9b9b,#7d7e80 60%,#8b8c8d)}
.hero-panels{position:absolute;left:0;top:0}
.hero-box{position:absolute;left:299px;top:62px;width:369px;height:165px;background:rgba(59,94,157,.72);color:var(--white);padding:16px 18px}
.hero-box h1{font-size:16.5px;line-height:22px;letter-spacing:.5px}
.hero-box p{font-size:10.5px;line-height:14px;margin-top:16px}
.hero-arrow{position:absolute;top:154px;width:34px;height:34px;border:1.5px solid rgba(255,255,255,.8);border-radius:50%;color:var(--white);text-align:center;line-height:30px;font-size:14px}
.dots{position:absolute;left:324px;top:301px;display:flex;gap:4px}
.dots span{width:7px;height:7px;border-radius:50%;border:1px solid var(--orange)}
.dots span:first-child{background:var(--orange)}

/* search */
.search{height:121px;background:var(--blue)}
.field{position:absolute;height:32px;background:var(--white);font-size:10px;color:#555;line-height:32px;padding-left:14px}
.field.select::after{content:"";position:absolute;right:14px;top:14px;border:4px solid transparent;border-top-color:#333}
.btn-search{position:absolute;left:727px;top:69px;width:220px;height:32px;background:var(--orange);color:var(--white);font-size:10px;font-weight:700;text-align:center;line-height:32px}

/* about */
.about{height:430px}
.about .stripes{position:absolute;left:0;top:0}
.about h2{position:absolute;left:629px;top:48px;font-size:27px;letter-spacing:1px}
.about p{position:absolute;left:629px;top:110px;width:330px;font-size:16px;line-height:27px}
.about .brand{position:absolute;left:254px;top:305px;font-size:24px}

/* services */
.services{height:248px;background:var(--orange)}
.services .left{position:absolute;left:0;top:0;width:506px;height:248px;background:var(--blue)}
.services h3{position:absolute;left:252px;top:80px;font-size:22px;font-weight:400;color:var(--white)}
.services h2{position:absolute;left:252px;top:118px;font-size:29px;color:var(--orange);letter-spacing:1.5px}
.vertical-brand{position:absolute;left:368px;top:112px;width:240px;transform:rotate(90deg);text-align:center;font-size:19px;font-weight:700;color:var(--white);letter-spacing:2px;line-height:24px}
.service-list{position:absolute;left:592px;top:40px;list-style:none}
.service-list li{height:37px;font-size:14px;font-weight:700;color:var(--white);display:flex;align-items:center}
.service-list li svg{margin-right:20px}
.service-list li em{font-style:normal;color:var(--blue);margin-left:5px}

/* products */
.products{height:902px}
.tabs{position:absolute;left:506px;top:116px;display:flex;font-size:9px;font-weight:700}
.tabs span{width:93px;height:24px;line-height:24px;text-align:center;background:#555a66;color:var(--white)}
.tabs span.on{background:var(--orange);color:var(--ink)}
.card{position:absolute;width:221px;height:301px;background:var(--blue);color:var(--white);text-align:center;box-shadow:0 3px 8px rgba(0,0,0,.25)}
.card .photo{position:absolute;left:0;top:0;width:221px;height:160px;clip-path:polygon(0 0,100% 0,100% 82%,50% 100%,0 82%)}
.card h4{position:absolute;top:178px;width:100%;font-size:13px;letter-spacing:.5px}
.card .desc{position:absolute;top:200px;left:15px;width:191px;font-size:8.5px;line-height:11px}
.card .price{position:absolute;top:234px;width:100%;font-size:13px;color:var(--orange)}
.card .view{position:absolute;left:17px;top:262px;width:90px;height:22px;background:var(--orange);font-size:8px;line-height:22px}
.card .cart{position:absolute;right:17px;top:262px;width:24px;height:22px;background:var(--orange)}
.view-more{position:absolute;left:538px;top:822px;width:132px;height:35px;border:1px solid var(--blue);color:var(--blue);font-size:13px;font-weight:700;text-align:center;line-height:33px}

/* strength */
.strength{height:335px;background:var(--light)}
.stat{position:absolute;top:130px;width:180px;margin-left:-90px;text-align:center}
.stat b{position:absolute;left:0;top:48px;width:180px;font-size:27px}
.stat span{display:block;margin-top:20px;font-size:15px;letter-spacing:1px}

/* industries */
.industries{height:422px;background:linear-gradient(100deg,#b9c0c6,#d9d6d2 40%,#e9ddd3 70%,#c7cbd0)}
.industries .section-title{top:46px}
.tile{position:absolute;top:157px;width:159px;height:174px;background:var(--orange);color:var(--white);font-size:14.5px;font-weight:700;line-height:29px;text-align:center;display:flex;align-items:center;justify-content:center;white-space:nowrap}

/* newsletter */
.newsletter{height:305px;background:var(--blue)}
.newsletter .photo{position:absolute;left:667px;top:0;width:533px;height:305px;background:linear-gradient(135deg,#3a3b3e,#1f2022 60%,#2c2d30)}
.newsletter h3{position:absolute;left:255px;top:62px;font-size:17px;color:var(--white);letter-spacing:1.5px}
.newsletter p{position:absolute;left:255px;top:87px;font-size:10px;color:var(--white)}
.email{position:absolute;left:254px;top:151px;width:276px;height:32px;background:var(--white);font-size:8px;color:#777;line-height:32px;padding-left:14px}
.signup{position:absolute;left:530px;top:151px;width:119px;height:32px;background:var(--orange);color:var(--white);font-size:9px;font-weight:700;text-align:center;line-height:32px}
.socials{position:absolute;display:flex;gap:14px}
.socials i{width:10px;height:10px;border-radius:50%;background:#8aa1c9;display:block}

/* testimonials */
.testimonials{height:398px}
.quote{position:absolute;top:130px;width:319px;height:183px;background:var(--blue);color:var(--white);padding:22px 24px}
.quote .avatar{position:absolute;left:24px;top:22px;width:38px;height:38px;border-radius:50%;background:#c9cdd4}
.quote .name{position:absolute;left:72px;top:26px;font-size:13px;color:var(--orange)}
.quote .loc{position:absolute;left:72px;top:46px;font-size:8px}
.quote .text{position:absolute;left:24px;top:80px;width:270px;font-size:7.5px;line-height:16px}
.quote .date{position:absolute;left:24px;top:158px;font-size:7px;color:var(--orange)}
.slider-dots{position:absolute;left:563px;top:342px;display:flex;gap:6px}
.slider-dots span{width:13px;height:13px;background:#8b8d93}
.slider-dots span.on{width:16px;height:16px;background:var(--orange);margin-top:-2px}

/* contact */
.contact{height:331px;background:var(--light)}
.contact h2{position:absolute;left:254px;top:45px;font-size:29px;color:var(--orange);letter-spacing:1px}
.contact .addr{position:absolute;left:254px;top:110px;font-size:17px;line-height:29px;color:var(--blue)}
.contact .addr b{font-weight:700}
.contact .reach{position:absolute;left:254px;top:223px;font-size:17px;line-height:29px;color:var(--blue);font-weight:700}
.map{position:absolute;left:549px;top:0;width:651px;height:331px;background:linear-gradient(160deg,#eaeae5,#f2f1ec 50%,#e4e6e2)}

/* footer */
.site-footer{height:167px;background:var(--dark)}
.to-top{position:absolute;left:587px;top:3903px;width:28px;height:28px;border-radius:50%;background:var(--orange);z-index:5}
.foot-links{position:absolute;left:255px;top:68px;display:flex;gap:18px;font-size:9.5px;color:var(--white)}
.copyright{position:absolute;left:255px;top:142px;display:flex;gap:24px;font-size:7.5px;color:#c9cad0}
</style>
</head>
<body>

<header class="topbar">
  <div class="brand">VALTIRO.NET</div>
  <div class="badge"><b>WE ARE LARGEST</b>STOCKIEST OF DIESEL<br>ENGINE SPARE PARTS</div>
  <div class="cart-box">
    <svg width="18" height="14" viewBox="0 0 18 14"><path d="M1 1h3l2 8h9l2-6H5" fill="none" stroke="#fff" stroke-width="1.5"/><circle cx="7" cy="12" r="1.3" fill="#fff"/><circle cx="14" cy="12" r="1.3" fill="#fff"/></svg>
    <div>01</div>
  </div>
  <div class="contact-top" style="top:8px"><i></i>info@valtiro.net</div>
  <div class="contact-top" style="top:30px;font-size:14px;font-weight:700"><i style="border-radius:50%"></i>000-111-2222</div>
</header>

<nav class="mainnav">
  <ul>
    <li class="active">HOME</li><li>STOCKIEST</li><li>DIESEL ENGINE</li><li>MARINE</li><li>POWER PLANTS</li><li>SPARE PARTS</li><li>ABOUT</li><li>CONTACT</li>
  </ul>
</nav>

<section class="hero" role="img" aria-label="Photo of a connecting rod on a textured workshop surface">
  <svg class="hero-panels" width="1200" height="344" role="img" aria-label="Close-up photos of connecting rods">
    <defs>
      <linearGradient id="metal" x1="0" y1="0" x2="1" y2="1"><stop offset="0" stop-color="#c9cbcd"/><stop offset=".5" stop-color="#8f9296"/><stop offset="1" stop-color="#b3b5b7"/></linearGradient>
      <linearGradient id="metal2" x1="0" y1="0" x2="1" y2="0"><stop offset="0" stop-color="#6f8ba8"/><stop offset=".5" stop-color="#b7b9ba"/><stop offset="1" stop-color="#a08a6a"/></linearGradient>
    </defs>
    <polygon points="806,0 1200,0 1200,344 770,344" fill="var(--blue)"/>
    <polygon points="848,0 1200,0 1200,99 818,99" fill="url(#metal)"/>
    <polygon points="816,107 1200,107 1200,223 782,223" fill="url(#metal2)"/>
    <polygon points="780,234 1200,234 1200,344 776,344" fill="url(#metal)"/>
    <polygon points="808,0 828,0 786,344 772,344" fill="#fff"/>
  </svg>
  <div class="hero-box">
    <h1>WE ARE ONE OF THE LARGEST STOCKIEST OF DIESEL ENGINE SPARE PARTS</h1>
    <p>When it comes to used parts, we put quality and customer service first, making sure our customers get the right working parts they need the first time.</p>
  </div>
  <div class="hero-arrow" style="left:254px">&#8249;</div>
  <div class="hero-arrow" style="left:736px">&#8250;</div>
  <div class="dots"><span></span><span></span><span></span></div>
</section>

<section class="search">
  <div class="field select" style="left:252px;top:19px;width:219px">Select Parts Type</div>
  <div class="field select" style="left:490px;top:19px;width:218px">Select Make Company</div>
  <div class="field select" style="left:727px;top:19px;width:220px">Select Model</div>
  <div class="field" style="left:252px;top:69px;width:456px">Enter Keywords</div>
  <div class="btn-search">SEARCH</div>
</section>

<section class="about">
  <svg class="stripes" width="600" height="430">
    <polygon points="0,0 588,0 550,60 510,430 0,430" fill="#f3f4f6"/>
    <rect x="280" y="120" width="210" height="160" fill="#555a62"/>
    <rect x="255" y="73" width="232" height="179" fill="#d9cdb2" role="img" aria-label="Photo of two connecting rods on a wooden board"/>
    <polyline points="565,134 565,229 545,280 565,324" fill="none" stroke="var(--blue)" stroke-width="2"/>
    <g fill="#fff" stroke="var(--blue)" stroke-width="2">
      <polygon points="565,110 586,122 586,146 565,158 544,146 544,122"/>
      <polygon points="545,205 566,217 566,241 545,253 524,241 524,217"/>
      <polygon points="528,300 549,312 549,336 528,348 507,336 507,312"/>
    </g>
    <g fill="var(--blue)"><circle cx="565" cy="134" r="8"/><circle cx="545" cy="229" r="8"/><circle cx="528" cy="324" r="8"/></g>
  </svg>
  <div class="brand">VALTIRO.NET</div>
  <h2>ABOUT VALTIRO</h2>
  <p>Lorem ipsum dolor sit amet, consectetur adipiscing elit, sed do eiusmod tempor incididunt ut labore et dolore magna aliqua. Ut enim ad minim veniam, quis nostrud exercitation ullamco laboris nisi ut aliquip ex ea commodo consequat. Duis aute irure dolor in reprehenderit in voluptate velit esse cillum dolore eu fugiat nulla pariatur.</p>
</section>

<section class="services">
  <div class="left"></div>
  <h3>OUR POPULAR</h3>
  <h2>SERVICES</h2>
  <div class="vertical-brand">VALTIRO.NET</div>
  <ul class="service-list">
    <li><svg width="20" height="18"><path d="M2 9l6 6L18 2" fill="none" stroke="var(--blue)" stroke-width="3"/></svg>DIESEL ENGINE FOR<em>MARINE</em></li>
    <li><svg width="20" height="18"><path d="M2 9l6 6L18 2" fill="none" stroke="var(--blue)" stroke-width="3"/></svg>DIESEL ENGINE FOR<em>POWER PLANTS</em></li>
    <li><svg width="20" height="18"><path d="M2 9l6 6L18 2" fill="none" stroke="var(--blue)" stroke-width="3"/></svg>DIESEL ENGINE FOR<em>SINGLE PRODUCT</em></li>
    <li><svg width="20" height="18"><path d="M2 9l6 6L18 2" fill="none" stroke="var(--blue)" stroke-width="3"/></svg>DIESEL ENGINE FOR<em>SPARE PARTS</em></li>
    <li><svg width="20" height="18"><path d="M2 9l6 6L18 2" fill="none" stroke="var(--blue)" stroke-width="3"/></svg>DIESEL ENGINE FOR<em>CONNECTING RODS</em></li>
  </ul>
</section>

<section class="products">
  <h2 class="section-title" style="top:36px">OUR PRODUCTS</h2>
  <div class="title-mark" style="top:82px"></div>
  <div class="tabs"><span class="on">MARINE</span><span>POWER PLANTS</span></div>

  <article class="card" style="left:252px;top:167px"><div class="photo" role="img" aria-label="Connecting rod product photo" style="background:linear-gradient(135deg,#b6b9bd,#7b7f85)"></div><h4>MARINE PRODUCT</h4><div class="desc">Diesel Engine Single product Single Spare Parts Sales</div><div class="price">$300.00</div><div class="view">VIEW DETAILS</div><div class="cart"></div></article>
  <article class="card" style="left:490px;top:167px"><div class="photo" role="img" aria-label="Connecting rod product photo" style="background:linear-gradient(135deg,#8c8f92,#5f6266)"></div><h4>MARINE PRODUCT</h4><div class="desc">Diesel Engine Single product Single Spare Parts Sales</div><div class="price">$450.00</div><div class="view">VIEW DETAILS</div><div class="cart"></div></article>
  <article class="card" style="left:727px;top:167px"><div class="photo" role="img" aria-label="Connecting rod product photo" style="background:linear-gradient(135deg,#7a7470,#b1aaa2)"></div><h4>MARINE PRODUCT</h4><div class="desc">Diesel Engine Single product Single Spare Parts Sales</div><div class="price">$800.00</div><div class="view">VIEW DETAILS</div><div class="cart"></div></article>
  <article class="card" style="left:252px;top:484px"><div class="photo" role="img" aria-label="Connecting rod product photo" style="background:linear-gradient(135deg,#d9ccb0,#8d8a84)"></div><h4>MARINE PRODUCT</h4><div class="desc">Diesel Engine Single product Single Spare Parts Sales</div><div class="price">$300.00</div><div class="view">VIEW DETAILS</div><div class="cart"></div></article>
  <article class="card" style="left:490px;top:484px"><div class="photo" role="img" aria-label="Connecting rod product photo" style="background:linear-gradient(135deg,#8b8580,#4e4a48)"></div><h4>MARINE PRODUCT</h4><div class="desc">Diesel Engine Single product Single Spare Parts Sales</div><div class="price">$800.00</div><div class="view">VIEW DETAILS</div><div class="cart"></div></article>
  <article class="card" style="left:727px;top:484px"><div class="photo" role="img" aria-label="Connecting rod product photo" style="background:linear-gradient(135deg,#c9b23a,#6f7690)"></div><h4>MARINE PRODUCT</h4><div class="desc">Diesel Engine Single product Single Spare Parts Sales</div><div class="price">$450.00</div><div class="view">VIEW DETAILS</div><div class="cart"></div></article>

  <div class="view-more">VIEW MORE</div>
</section>

<section class="strength">
  <h2 class="section-title" style="top:40px">OUR STRENGTH</h2>
  <div class="title-mark" style="top:86px"></div>
  <div class="stat" style="left:333px"><svg width="130" height="130" viewBox="0 0 130 130"><circle cx="65" cy="65" r="58" fill="none" stroke="var(--blue)" stroke-width="9"/><path d="M65 7 A58 58 0 0 1 119 44" fill="none" stroke="var(--orange)" stroke-width="9"/></svg><b>200+</b><span>CUSTOMERS</span></div>
  <div class="stat" style="left:511px"><svg width="130" height="130" viewBox="0 0 130 130"><circle cx="65" cy="65" r="58" fill="none" stroke="var(--blue)" stroke-width="9"/><path d="M65 7 A58 58 0 0 1 123 65" fill="none" stroke="var(--orange)" stroke-width="9"/></svg><b>1500+</b><span>STOCKS</span></div>
  <div class="stat" style="left:691px"><svg width="130" height="130" viewBox="0 0 130 130"><circle cx="65" cy="65" r="58" fill="none" stroke="var(--blue)" stroke-width="9"/><path d="M65 7 A58 58 0 0 1 90 117" fill="none" stroke="var(--orange)" stroke-width="9"/></svg><b>15+</b><span>DISTRIBUTORS</span></div>
  <div class="stat" style="left:869px"><svg width="130" height="130" viewBox="0 0 130 130"><circle cx="65" cy="65" r="58" fill="none" stroke="var(--blue)" stroke-width="9"/><path d="M65 7 A58 58 0 0 1 113 33" fill="none" stroke="var(--orange)" stroke-width="9"/></svg><b>30+</b><span>COUNTRIES</span></div>
</section>

<section class="industries" role="img" aria-label="Faded photo of a connecting rod big end behind the service tiles">
  <h2 class="section-title">INDUSTRIES WE SERVE</h2>
  <div class="title-mark" style="top:92px"></div>
  <div class="tile" style="left:253px">STOCKIEST OF<br>MARINE<br>SPARE PARTS</div>
  <div class="tile" style="left:431px">STOCKIEST OF<br>POWER PLANTS<br>SPARE PARTS</div>
  <div class="tile" style="left:610px">STOCKIEST OF<br>SINGLE<br>PRODUCT</div>
  <div class="tile" style="left:788px">STOCKIEST OF<br>CONNECTING<br>RODS</div>
</section>

<section class="newsletter">
  <div class="photo" role="img" aria-label="Video still of a connecting rod on a dark background">
    <svg class="abs" style="left:233px;top:119px" width="68" height="68"><circle cx="34" cy="34" r="31" fill="none" stroke="#fff" stroke-width="3"/><path d="M26 20v28l22-14z" fill="none" stroke="#fff" stroke-width="3"/></svg>
  </div>
  <h3>SUBSCRIBE TO OUR NEWSLETTER</h3>
  <p>Lorem ipsum dolor sit amet, consectetur adipisi cing elit.</p>
  <div class="email">Enter Your Email Address</div>
  <div class="signup">SIGN UP NOW</div>
  <div class="socials" style="left:254px;top:226px"><i></i><i></i><i></i></div>
</section>

<section class="testimonials">
  <h2 class="section-title" style="top:36px">WHAT OUR CLIENT SAYING</h2>
  <div class="title-mark" style="top:82px"></div>
  <article class="quote" style="left:264px">
    <div class="avatar"></div><div class="name">Daniel Reyes</div><div class="loc">USA</div>
    <p class="text">Lorem ipsum dolor sit amet, consectetur adipiscing elit, sed do eiusmod tempor incididunt ut labore et dolore magna aliqua. Ut enim ad minim veniam, quis nostrud exercitation ullamco laboris nisi ut aliquip ex ea commodo consequat.</p>
    <div class="date">16 Dec 2020</div>
  </article>
  <article class="quote" style="left:618px">
    <div class="avatar"></div><div class="name">Daniel Reyes</div><div class="loc">USA</div>
    <p class="text">Lorem ipsum dolor sit amet, consectetur adipiscing elit, sed do eiusmod tempor incididunt ut labore et dolore magna aliqua. Ut enim ad minim veniam, quis nostrud exercitation ullamco laboris nisi ut aliquip ex ea commodo consequat.</p>
    <div class="date">16 Dec 2020</div>
  </article>
  <div class="slider-dots"><span class="on"></span><span></span><span></span><span></span></div>
</section>

<section class="contact">
  <h2>CONTACT US</h2>
  <div class="addr"><b>VALTIRO.NET</b><br>123, Road,<br>CA, USA</div>
  <div class="reach">CALL: 000-000-0000<br>EMAIL: info@valtiro.net<br>WEB: www.valtiro.net</div>
  <div class="map" role="img" aria-label="Street map showing the office location"></div>
</section>

<div class="to-top"><svg width="28" height="28"><path d="M14 20V9M9 13l5-5 5 5" fill="none" stroke="#fff" stroke-width="2"/></svg></div>

<footer class="site-footer">
  <div class="foot-links"><span>Home</span><span>Stockiest</span><span>Disel Engine</span><span>Marine</span><span>Power Plants</span><span>Spare Parts</span><span>About</span><span>Contactus</span></div>
  <div class="socials" style="left:846px;top:70px"><i style="background:#9a9ba3"></i><i style="background:#9a9ba3"></i><i style="background:#9a9ba3"></i></div>
  <div class="copyright"><span>Copyright © 2020 Valtiro.net</span><span>Terms &amp; Conditions</span><span>Privacy Policy</span></div>
</footer>

</body>
</html>
```